Label Design for Nuts package*

Develop the design for a label for nuts sold in a paperbag.

you can find our website here: www.brotkorn-snack.de.
Here comes the link to our catalogue: https://www.blattwerk-docs.com/de/document/read/48172095/brotkorn-premium-snacks-gesamtkatalog-2019

With this product we are targeting private customers who want to buy nuts with plastic free packaging online.
The colours of the label should fit the brown paper bag.

```html
<!DOCTYPE html>
<html lang="en">
<head>
<meta charset="utf-8">
<title>brotkorn – Premium Wallnut label</title>
<link rel="stylesheet" href="https://fonts.googleapis.com/css2?family=Anton&family=Open+Sans:wght@600;700&family=Comfortaa:wght@500&display=swap">
<style>
  :root {
    --backdrop: #e8705f;
    --kraft: #bb9d72;
    --kraft-light: #c6a97f;
    --kraft-dark: #a98b61;
    --ink: #3a1d19;
    --ink-deep: #2a1714;
    --cream: #ede3cf;
    --window-light: #c9a987;
    --window-dark: #6e5440;
    --paper-white: #f4efe6;
  }
  * { box-sizing: border-box; margin: 0; padding: 0; }
  html, body { width: 1200px; height: 834px; overflow: hidden; }
  body {
    background: var(--backdrop);
    font-family: "Open Sans", Arial, sans-serif;
    color: var(--ink);
    position: relative;
  }
  .label {
    position: absolute;
    left: 375px; top: 27px;
    width: 450px; height: 780px;
    border-radius: 18px 18px 6px 6px;
    overflow: hidden;
  }
  .label__paper {
    position: absolute; inset: 0;
    background: radial-gradient(ellipse at 50% 40%, var(--kraft-light), var(--kraft) 60%, var(--kraft-dark));
  }
  .brand-tab {
    position: absolute;
    left: 159px; top: 0;
    width: 130px; height: 226px;
    background: var(--cream);
    display: flex; align-items: flex-end; justify-content: center;
    padding-bottom: 42px;
  }
  .brand-tab__name {
    font-family: "Comfortaa", sans-serif;
    font-weight: 500;
    font-size: 19px;
    color: var(--ink);
    letter-spacing: 0.5px;
  }
  .product-kicker {
    position: absolute; left: 0; right: 0; top: 254px;
    text-align: center;
    font-weight: 700; font-size: 29px; letter-spacing: 0.5px;
  }
  .product-name {
    position: absolute; left: 0; right: 0; top: 278px;
    text-align: center;
    font-family: "Anton", Impact, sans-serif;
    font-size: 86px; line-height: 1.1;
    letter-spacing: 11px;
    padding-left: 11px;
    color: var(--ink-deep);
  }
  .claims {
    position: absolute; top: 450px;
    font-weight: 600; line-height: 1.3;
  }
  .claims--left {
    left: 56px;
    border-left: 2px solid var(--ink);
    padding-left: 6px;
    font-size: 18px;
  }
  .claims--right {
    right: 44px; top: 458px;
    border-right: 2px solid var(--ink);
    padding-right: 6px;
    text-align: right;
    font-size: 14px; line-height: 1.55;
    text-transform: uppercase;
  }
  .window {
    position: absolute;
    left: 63px; top: 543px;
    width: 337px; height: 186px;
    border-radius: 18px;
    background: radial-gradient(circle at 40% 45%, var(--window-light), #a88566 55%, var(--window-dark));
  }
  .weight-band {
    position: absolute; left: 0; right: 0; bottom: 0;
    height: 48px;
    background: var(--ink-deep);
    display: flex; align-items: center; justify-content: flex-end;
    padding-right: 36px;
  }
  .weight-band__text {
    color: var(--paper-white);
    font-weight: 700; font-size: 17px; letter-spacing: 0.3px;
  }
</style>
</head>
<body>
  <main class="label">
    <div class="label__paper" role="img" aria-label="Kraft paper background with faint line drawings of walnuts"></div>

    <div class="brand-tab">
      <span class="brand-tab__name">brotkorn</span>
    </div>

    <p class="product-kicker">PREMIUM</p>
    <h1 class="product-name">WALLNUT</h1>

    <ul class="claims claims--left" style="list-style:none">
      <li>Crunchy</li>
      <li>Nutritious</li>
      <li>Healthy</li>
    </ul>

    <ul class="claims claims--right" style="list-style:none">
      <li>Moisture free nuts</li>
      <li>High in protein</li>
      <li>&amp; Energy</li>
    </ul>

    <div class="window" role="img" aria-label="Window showing whole walnuts in their shells"></div>

    <div class="weight-band">
      <span class="weight-band__text">Net. wt. 300gm</span>
    </div>
  </main>
</body>
</html>
```